Larkmere Hall Business Cards design with a logo

I want two Business cards designed with a very modern contemporary logo UNING 1920'S FONT STYLES with the following details

Address:
Larkmere Hall
17 Penwick Lane
Ashcombe
K31 5TB

Details for card 1

Name: Desmond Hartley
email: Desmond.hartley@larkmere.example
Tel : +971 55 318 2964
Tel +44 7700 900 318

Details Card 2

Name: Desmond Hartley
email: Oliver.brandt@larkmere.example
Tel : +971 55 604 1387

Larkmere hall is a house that was built around 1880 and was used extensively in the 1920's for entertaining and parties in the arts scene, the house again will be resurrected to a modern entertainment venue

If you have any questions feel free to ask

Target Market(s)

The market for this is the young modern crowd

Industry/Entity Type

Entertainment Industry

Contact Information for Business Card

Address:
Larkmere Hall
17 Penwick Lane
Ashcombe
K31 5TB

Details for card 1

Name: Desmond Hartley
Tel : +971 55 318 2964
Tel +44 7700 900 318

Details Card 2

Name: Oliver Brandt
Tel : +971 55 604 1387

Logo Text

Larkmere Hall

Font styles to use
Other font styles liked:
• 1920'S FONT STULES

Requirements
Must have
• Modern Contemporary, whilst taking into consideration the age of the house as detailed above. YOU MUT BE USING 1920'S FONT STYLES
Nice to have
• 1920'S FONT STYLES see attached image if a suggestion
Should not have
• Should not look old or dated

```html
<!DOCTYPE html>
<html lang="en">
<head>
<meta charset="utf-8">
<title>Larkmere Hall — Business Cards</title>
<link href="https://fonts.googleapis.com/css2?family=Playfair+Display:ital,wght@0,400;0,900;1,700;1,900&display=swap" rel="stylesheet">
<style>
  :root {
    --backdrop: #262626;
    --card: #0b0b0b;
    --card-edge: #1a1a1a;
    --gold: #d9ad2e;
  }
  * { margin: 0; padding: 0; box-sizing: border-box; }
  html, body { width: 1200px; height: 900px; overflow: hidden; background: var(--backdrop); }
  .canvas { position: relative; width: 1200px; height: 900px; overflow: hidden; font-family: "Playfair Display", Georgia, serif; color: var(--gold); }

  .card {
    position: absolute; width: 520px; height: 300px;
    background: var(--card);
    border: 1px solid var(--card-edge);
    box-shadow: 0 18px 40px rgba(0,0,0,.55);
  }
  .card--back { left: 620px; top: 90px; }
  .card--front { left: 70px; top: 360px; }

  .wordmark { display: flex; align-items: center; justify-content: center; gap: 12px; font-weight: 900; text-transform: uppercase; letter-spacing: .5px; color: var(--gold); white-space: nowrap; }
  .wordmark__square { width: 12px; height: 12px; background: var(--gold); flex: none; }

  .card--back .wordmark { position: absolute; left: 0; right: 0; top: 100px; font-size: 40px; }
  .address { position: absolute; left: 0; right: 0; top: 190px; display: flex; justify-content: center; align-items: center; gap: 8px; font-style: italic; font-weight: 700; font-size: 17px; }

  .card--front .wordmark { position: absolute; left: 0; right: 0; top: 52px; font-size: 30px; }
  .holder { position: absolute; left: 0; right: 0; top: 118px; text-align: center; font-style: italic; font-weight: 900; font-size: 32px; }
  .rule { position: absolute; left: 210px; width: 100px; top: 172px; height: 3px; background: var(--gold); }
  .contacts { position: absolute; left: 20px; right: 20px; top: 214px; list-style: none; display: flex; flex-wrap: wrap; justify-content: center; gap: 10px 20px; font-style: italic; font-weight: 700; font-size: 14px; }
  .contact { display: flex; align-items: center; gap: 6px; white-space: nowrap; }
  .icon { width: 14px; height: 14px; flex: none; }

  .brand-mark { position: absolute; right: 40px; bottom: 110px; }
  .brand-mark .wordmark { font-size: 40px; }
</style>
</head>
<body>
<main class="canvas">

  <section class="card card--back" aria-label="Business card, reverse">
    <div class="wordmark"><span class="wordmark__square"></span>Larkmere Hall</div>
    <p class="address">
      <svg class="icon" viewBox="0 0 16 16" aria-hidden="true"><path d="M8 1a5 5 0 0 0-5 5c0 4 5 9 5 9s5-5 5-9a5 5 0 0 0-5-5zm0 7a2 2 0 1 1 0-4 2 2 0 0 1 0 4z" fill="var(--gold)"/></svg>
      17 Penwick Lane, Ashcombe, K31 5TB
    </p>
  </section>

  <section class="card card--front" aria-label="Business card, front">
    <div class="wordmark"><span class="wordmark__square"></span>Larkmere Hall</div>
    <h1 class="holder">Desmond Hartley</h1>
    <div class="rule"></div>
    <ul class="contacts">
      <li class="contact">
        <svg class="icon" viewBox="0 0 16 16" aria-hidden="true"><rect x="1" y="3" width="14" height="10" fill="none" stroke="var(--gold)" stroke-width="1.6"/><path d="M1 3l7 6 7-6" fill="none" stroke="var(--gold)" stroke-width="1.6"/></svg>
        Desmond.hartley@larkmere.example
      </li>
      <li class="contact">
        <svg class="icon" viewBox="0 0 16 16" aria-hidden="true"><rect x="4" y="1" width="8" height="14" rx="1.5" fill="none" stroke="var(--gold)" stroke-width="1.6"/><circle cx="8" cy="12.5" r="1" fill="var(--gold)"/></svg>
        +971 50 000 0417
      </li>
      <li class="contact">
        <svg class="icon" viewBox="0 0 16 16" aria-hidden="true"><path d="M3 1.5l3 .5 1 3.5-2 1.5c1 2 2.5 3.5 4.5 4.5l1.5-2 3.5 1 .5 3c-7 1-13-5-12-12z" fill="var(--gold)"/></svg>
        +44 7700 900 318
      </li>
    </ul>
  </section>

  <div class="brand-mark">
    <div class="wordmark"><span class="wordmark__square"></span>Larkmere Hall</div>
  </div>

</main>
</body>
</html>
```